Nana Bo's needs your help creating a clean, simple, possibly vintage style label for a natural rem...

We need a label for a new product to be sold in local stores. It will be a bottle of fresh Elderberry Syrup which is a natural remedy for the flu, colds, and allergies. Our syrup is different from others in the market as it is fresh, needs to be refrigerated, and does not include preservatives, added sugar, alcohol, or anything artificial. We would like a label with easy to read text, with a clean or vintage look. We would like a 3 inch by 3 inch circle front label with mostly text, not too busy, and possibly a branch of elderberries may be included. We also need a 3 inch by 3 inch circle label for the back of the bottle with the nutrition facts, ingredients, dosage, and specific text. Both labels should be lighter in (background) color to stand out from the dark purple liquid inside. We're leaning towards black for the main text, but open to other ideas that are neutral and not too flashy.The final design should be clear, clean, making the main text visible if in a grocery store refrigerator. It should appeal to all, but mostly to natural minded mothers.
Natural minded mothers

```html
<!DOCTYPE html>
<html lang="en">
<head>
<meta charset="utf-8">
<title>Nana Bo's Elderberry Syrup – Front and Back Labels</title>
<link href="https://fonts.googleapis.com/css2?family=Oswald:wght@300;400;500;600&family=Arimo:ital,wght@0,400;0,700;1,700&family=Kaushan+Script&display=swap" rel="stylesheet">
<style>
  :root {
    --paper: #ffffff;
    --night: #000000;
    --kraft: #e2c4a4;
    --label-white: #ffffff;
    --ink: #141414;
    --body-ink: #222222;
    --plum: #3b2168;
    --leaf: #3f7a4a;
    --berry: #2a1d3d;
  }
  html, body {
    margin: 0;
    padding: 0;
    width: 1200px;
    height: 1200px;
    overflow: hidden;
    background: var(--paper);
  }
  .sheet { display: block; width: 1200px; height: 1200px; }
  .band-light { fill: var(--paper); }
  .band-dark { fill: var(--night); }
  .face-kraft { fill: var(--kraft); }
  .face-white { fill: var(--label-white); }
  .ring-thin { fill: none; stroke: var(--ink); stroke-width: 1.3; }
  .ring-bold { fill: none; stroke: var(--ink); stroke-width: 2.6; }
  .arc-claim { font-family: "Oswald", sans-serif; font-weight: 500; font-size: 29px; fill: var(--ink); }
  .net-weight { font-family: "Oswald", sans-serif; font-weight: 300; font-size: 22px; fill: var(--ink); }
  .dot { fill: var(--ink); }
  .brand-script { font-family: "Kaushan Script", cursive; fill: var(--plum); }
  .product-name { font-family: "Oswald", sans-serif; font-weight: 600; font-size: 80px; fill: var(--ink); }
  .product-type { font-family: "Oswald", sans-serif; font-weight: 500; font-size: 44px; fill: var(--ink); }
  .product-claim { font-family: "Oswald", sans-serif; font-weight: 300; font-size: 17px; fill: var(--ink); }
  .branch-art { fill: url(#branchTone); }
  .intro { font-family: "Arimo", sans-serif; font-size: 12.5px; fill: var(--body-ink); }
  .nf-title { font-family: "Arimo", sans-serif; font-weight: 700; font-size: 22px; fill: var(--ink); }
  .nf-small { font-family: "Arimo", sans-serif; font-size: 8.5px; fill: var(--ink); }
  .nf-bold { font-family: "Arimo", sans-serif; font-weight: 700; font-size: 8.5px; fill: var(--ink); }
  .nf-tiny { font-family: "Arimo", sans-serif; font-weight: 700; font-size: 6.5px; fill: var(--ink); }
  .nf-foot { font-family: "Arimo", sans-serif; font-size: 5.6px; fill: var(--ink); }
  .nf-rule { fill: var(--ink); }
  .nf-hair { stroke: var(--ink); stroke-width: 0.8; }
  .nf-box { fill: none; stroke: var(--ink); stroke-width: 1.4; }
  .info { font-family: "Arimo", sans-serif; font-size: 10.5px; fill: var(--body-ink); }
  .info-head { font-family: "Arimo", sans-serif; font-weight: 700; font-size: 10.5px; fill: var(--ink); }
  .disclaimer-box { fill: none; stroke: var(--ink); stroke-width: 0.8; }
  .disclaimer { font-family: "Arimo", sans-serif; font-size: 7.8px; fill: var(--body-ink); }
  .storage { font-family: "Arimo", sans-serif; font-weight: 700; font-style: italic; font-size: 11.5px; fill: var(--ink); }
  .maker { font-family: "Arimo", sans-serif; font-size: 10.5px; fill: var(--body-ink); }
  .address { font-family: "Arimo", sans-serif; font-size: 10px; fill: var(--body-ink); }
</style>
</head>
<body>
<svg class="sheet" viewBox="0 0 1400 1400" xmlns="http://www.w3.org/2000/svg">
  <defs>
    <linearGradient id="branchTone" x1="0" y1="0" x2="0" y2="1">
      <stop offset="0" stop-color="#3f7a4a"/>
      <stop offset="1" stop-color="#2a1d3d"/>
    </linearGradient>
    <path id="claimArc" d="M -105.3 139.8 A 175 175 0 1 1 105.3 139.8"/>
    <path id="weightArc" d="M -186 0 A 186 186 0 0 0 186 0"/>

    <g id="labelRings">
      <circle class="ring-thin" r="208"/>
      <circle class="ring-bold" r="203"/>
    </g>

    <g id="frontLabel">
      <use href="#labelRings"/>
      <text class="arc-claim"><textPath href="#claimArc" textLength="868" lengthAdjust="spacing">MADE WITH ORGANIC ELDERBERRIES &amp; SPICES &amp; LOCAL TEXAS RAW HONEY</textPath></text>
      <circle class="dot" cx="-87" cy="155" r="5"/>
      <circle class="dot" cx="85" cy="155" r="5"/>
      <text class="net-weight" text-anchor="middle"><textPath href="#weightArc" startOffset="50%">NET WT 8 FL OZ</textPath></text>
      <text class="brand-script" x="0" y="-72" font-size="58" text-anchor="middle">Nana Bo's</text>
      <text class="product-name" x="0" y="20" text-anchor="middle" textLength="284" lengthAdjust="spacingAndGlyphs">ELDERBERRY</text>
      <text class="product-type" x="0" y="72" text-anchor="middle" textLength="130" lengthAdjust="spacing">SYRUP</text>
      <text class="product-claim" x="0" y="92" text-anchor="middle" textLength="136" lengthAdjust="spacing">IMMUNE BOOSTING*</text>
      <ellipse class="branch-art" cx="0" cy="130" rx="58" ry="30" role="img" aria-label="Illustrated branch of elderberries with green leaves"/>
    </g>

    <g id="backLabel">
      <use href="#labelRings"/>
      <ellipse class="branch-art" cx="-2" cy="-175" rx="32" ry="16" role="img" aria-label="Small illustrated elderberry sprig"/>
      <text class="intro" text-anchor="middle">
        <tspan x="0" y="-140">This delicious elderberry syrup boosts the</tspan>
        <tspan x="0" y="-125">immune system. It is a natural remedy for the</tspan>
        <tspan x="0" y="-110">flu, colds, and allergies.*</tspan>
      </text>

      <g class="nutrition-panel">
        <rect class="nf-box" x="-165" y="-97" width="177" height="166"/>
        <text class="nf-title" x="-162" y="-75" textLength="168" lengthAdjust="spacingAndGlyphs">Nutrition Facts</text>
        <text class="nf-small" x="-162" y="-65">Serving Size 1 TBSP</text>
        <text class="nf-small" x="-162" y="-55">Servings Per Container 16</text>
        <rect class="nf-rule" x="-162" y="-51" width="171" height="4.5"/>
        <text class="nf-tiny" x="-162" y="-40">Amount Per Serving</text>
        <line class="nf-hair" x1="-162" y1="-37" x2="9" y2="-37"/>
        <text class="nf-bold" x="-162" y="-28">Calories 20</text>
        <rect class="nf-rule" x="-162" y="-24" width="171" height="3"/>
        <text class="nf-tiny" x="8" y="-14" text-anchor="end">% Daily Value*</text>
        <line class="nf-hair" x1="-162" y1="-11" x2="9" y2="-11"/>
        <text class="nf-small" x="-162" y="-2"><tspan class="nf-bold">Total Fat</tspan> 0g</text>
        <text class="nf-bold" x="8" y="-2" text-anchor="end">0%</text>
        <line class="nf-hair" x1="-162" y1="1.5" x2="9" y2="1.5"/>
        <text class="nf-small" x="-162" y="11"><tspan class="nf-bold">Sodium</tspan> 4mg</text>
        <text class="nf-bold" x="8" y="11" text-anchor="end">0%</text>
        <line class="nf-hair" x1="-162" y1="14.5" x2="9" y2="14.5"/>
        <text class="nf-small" x="-162" y="24"><tspan class="nf-bold">Total Carbohydrate</tspan> 5g</text>
        <text class="nf-bold" x="8" y="24" text-anchor="end">2%</text>
        <line class="nf-hair" x1="-162" y1="27.5" x2="9" y2="27.5"/>
        <text class="nf-small" x="-152" y="36">Sugars 4g</text>
        <line class="nf-hair" x1="-162" y1="39.5" x2="9" y2="39.5"/>
        <text class="nf-small" x="-162" y="48"><tspan class="nf-bold">Protein</tspan> 0g</text>
        <text class="nf-bold" x="8" y="48" text-anchor="end">0%</text>
        <rect class="nf-rule" x="-162" y="51" width="171" height="4"/>
        <text class="nf-foot" x="-161" y="63">*Percent Daily Values are based on a 2,000 calorie diet.</text>
      </g>

      <g class="directions">
        <text class="info">
          <tspan x="21" y="-91"><tspan class="info-head">Ingredients:</tspan> distilled water,</tspan>
          <tspan x="21" y="-80">raw honey from North Texas,</tspan>
          <tspan x="21" y="-68">certified organic elderberries</tspan>
          <tspan x="21" y="-57">(sambucus nigra), certified</tspan>
          <tspan x="21" y="-45">organic ginger, certified organic</tspan>
          <tspan x="21" y="-34">cinnamon, certified organic cloves.</tspan>
        </text>
        <text class="info-head" x="21" y="-14">For immune support:</text>
        <text class="info">
          <tspan x="21" y="-3">Adults 1 tbsp / Children 1 tsp</tspan>
          <tspan x="21" y="8">once per day</tspan>
        </text>
        <text class="info-head" x="21" y="26">For cold and flu treatment:</text>
        <text class="info" x="21" y="41">Take one dose every 2-3 hours</text>
        <text class="info-head">
          <tspan x="21" y="56">DO NOT GIVE TO INFANTS</tspan>
          <tspan x="21" y="68">UNDER 1 YEAR OF AGE</tspan>
        </text>
      </g>

      <rect class="disclaimer-box" x="-165" y="73" width="330" height="27"/>
      <text class="disclaimer" text-anchor="middle">
        <tspan x="0" y="84">*This statement has not been evaluated by the Food and Drug Administration.</tspan>
        <tspan x="0" y="95">This product is not intended to diagnose, treat, cure, or prevent any disease.</tspan>
      </text>

      <text class="storage" x="0" y="125" text-anchor="middle">KEEP REFRIGERATED</text>
      <text class="maker" x="-90" y="152">Made with love by:</text>
      <text class="brand-script" x="5" y="155" font-size="22">Nana Bo's</text>
      <text class="address" x="0" y="174" text-anchor="middle">118 Oak Lane Millbrook, Texas 75000</text>
    </g>
  </defs>

  <rect class="band-light" x="0" y="0" width="1400" height="700"/>
  <rect class="band-dark" x="0" y="700" width="1400" height="700"/>

  <g class="label front kraft" transform="translate(400 325)">
    <circle class="face-kraft" r="215"/>
    <use href="#frontLabel"/>
  </g>
  <g class="label back kraft" transform="translate(1025 325)">
    <circle class="face-kraft" r="215"/>
    <use href="#backLabel"/>
  </g>

  <g class="label front white" transform="translate(400 1068)">
    <circle class="face-white" r="215"/>
    <use href="#frontLabel"/>
  </g>
  <g class="label back white" transform="translate(1025 1068)">
    <circle class="face-white" r="215"/>
    <use href="#backLabel"/>
  </g>
</svg>
</body>
</html>
```